I need a direct mail postcard made up for my marketing campaign

I am starting a marketing campaign and need a design for a post card. I own an iron door company and need to have before and after images on the post card to showcase what our work looks like. I have provided pictures to use below.

The design needs to be two sided. The logo should be on the front.

The tag line for this campaign is: Design the smile your home deserves.

Words to also use: Distinctive style, Work of Art, One-of-a-Kind, Elegant, Modern, Innovative, Unique

My information for the card
Name: Dean Harlowe
Phone number: (555)-318-2764
Email: Dean@wroughtgatestudio.example

The US postal system is very picky as to what can be sent in the mail. The only requirement they have is for the address. There needs to be a 2inch (50.8mm) by 4inch (101.6mm) blank space on the bottom right hand corner on the back of the card.

Target Market(s)

Home owners

Industry/Entity Type

Home Improvement

Font styles to use
Serif
Decorative

Colors
0555a3
ffffff
ec1f27

Requirements
Must have
• My logo, My contact information, before and after pictures
• Provided 3D images
Nice to have
• Words that describe iron doors
• A contrast between contemporary and ornate doors.

```html
<!DOCTYPE html>
<html lang="en">
<head>
<meta charset="utf-8">
<title>Wrought Gate Studio – Postcard</title>
<link rel="stylesheet" href="https://fonts.googleapis.com/css2?family=Michroma&family=Open+Sans:wght@400;600&family=Roboto:wght@500;700&display=swap">
<style>
  :root {
    --stage: #8a8a8a;
    --brand-blue: #1a5a93;
    --ink: #111111;
    --panel: #ececec;
    --paper: #ffffff;
    --wash: #eef2ec;
  }
  * { margin: 0; padding: 0; box-sizing: border-box; }
  html, body { width: 1200px; height: 1200px; overflow: hidden; background: var(--stage); }
  body { position: relative; font-family: "Open Sans", Arial, sans-serif; color: var(--ink); }

  .card { position: absolute; width: 793px; height: 510px; overflow: hidden; }

  /* Front */
  .card-front { left: 70px; top: 67px; background: var(--wash); }
  .front-photo { position: absolute; inset: 0;
    background: linear-gradient(90deg, #c9c7b2 0%, #3e5a2c 22%, #b8a88a 35%, #7a4a24 48%, #b8a88a 60%, #3e5a2c 75%, #c7c7b8 100%); }
  .front-overlay { position: absolute; inset: 0; }
  .tagline { position: absolute; left: 140px; top: 56px; font-family: "Roboto", Arial, sans-serif; font-weight: 700;
    font-size: 28px; color: var(--paper); letter-spacing: 0.4px; white-space: nowrap; text-shadow: 0 1px 3px rgba(0,0,0,0.4); }
  .front-brand { position: absolute; left: 22px; top: 418px; width: 92px; font-family: "Michroma", sans-serif;
    font-size: 8px; line-height: 1.35; color: var(--brand-blue); text-align: center; }
  .front-brand .dot { display: block; width: 22px; height: 22px; border-radius: 50%; background: var(--brand-blue); margin: 0 auto 6px; }
  .slogan { position: absolute; left: 127px; top: 437px; font-family: "Michroma", sans-serif; font-size: 23px;
    color: var(--ink); letter-spacing: 1.5px; white-space: nowrap; }
  .front-phone { position: absolute; left: 506px; top: 432px; font-family: "Michroma", sans-serif; font-size: 18.5px;
    color: var(--ink); letter-spacing: 1.5px; display: flex; align-items: center; gap: 18px; white-space: nowrap; }
  .front-email { position: absolute; right: 23px; top: 468px; font-size: 14px; letter-spacing: 1.2px; color: var(--ink); white-space: nowrap; }

  /* Back */
  .card-back { left: 343px; top: 622px; width: 794px; background: var(--paper); }
  .message-side { position: absolute; left: 0; top: 0; width: 523px; height: 510px; background: var(--panel); overflow: hidden; }
  .headline { position: absolute; left: 16px; top: 27px; width: 290px; font-family: "Michroma", sans-serif;
    font-size: 14.5px; line-height: 20px; color: var(--brand-blue); letter-spacing: 0.5px; font-weight: 400; }
  .body-copy { position: absolute; left: 16px; top: 72px; width: 282px; font-size: 10.5px; line-height: 14px;
    letter-spacing: 0.4px; text-align: justify; }
  .house-photo { position: absolute; left: 309px; top: 17px; width: 199px; height: 164px;
    background: linear-gradient(180deg, #e4e8ea 0%, #e4e8ea 30%, #b04a32 42%, #c98c5a 58%, #5e8a3a 72%, #c9c9c4 100%); }
  .info-band { position: absolute; left: 16px; top: 198px; width: 493px; height: 98px; background: var(--brand-blue);
    border-bottom-left-radius: 90px 70px; color: var(--paper); font-size: 7px; line-height: 9.4px; letter-spacing: 0.3px; }
  .info-band .col-left { position: absolute; left: 10px; top: 22px; width: 236px; text-align: center; }
  .info-band .divider { position: absolute; left: 254px; top: 14px; width: 2px; height: 79px; background: var(--paper); }
  .info-band .col-right { position: absolute; left: 262px; top: 22px; width: 220px; text-align: justify; }
  .lower-copy { position: absolute; left: 16px; top: 320px; width: 268px; font-size: 9.8px; line-height: 12.4px;
    letter-spacing: 0.4px; text-align: justify; }
  .portrait { position: absolute; left: 16px; top: 381px; width: 99px; height: 114px;
    background: linear-gradient(135deg, #6f7f8c 0%, #9aa6ae 50%, #2a3140 100%); }
  .portrait::after { content: ""; position: absolute; left: 6px; top: 9px; width: 87px; height: 98px; border: 3px solid var(--paper); }
  .contact-name { position: absolute; left: 128px; top: 416px; font-family: "Michroma", sans-serif; font-size: 14px; letter-spacing: 1.2px; white-space: nowrap; }
  .contact-phone { position: absolute; left: 128px; top: 443px; font-family: "Michroma", sans-serif; font-size: 11px;
    letter-spacing: 0.6px; display: flex; align-items: center; gap: 8px; color: #333; white-space: nowrap; }
  .contact-email { position: absolute; left: 128px; top: 466px; font-size: 8.3px; letter-spacing: 0.3px; white-space: nowrap; }
  .door-tile { position: absolute; top: 318px; width: 98px; height: 176px; border: 2px solid var(--brand-blue);
    border-bottom-left-radius: 38px; overflow: hidden; }
  .door-tile.before { left: 299px; background: linear-gradient(180deg, #e2d3a8 0%, #f2f2ee 12%, #ffffff 100%); }
  .door-tile.after { left: 410px; background: linear-gradient(180deg, #3a3a50 0%, #5a6270 40%, #2d6b2e 48%, #4a4a5c 60%, #2f2f3e 100%); }
  .door-tile .label { position: absolute; left: 0; right: 0; top: 133px; height: 24px; background: var(--brand-blue);
    color: var(--paper); font-family: "Roboto", Arial, sans-serif; font-weight: 700; font-size: 15px; letter-spacing: 1px;
    text-align: center; line-height: 24px; }
  .back-brand { position: absolute; left: 550px; top: 28px; width: 62px; font-family: "Michroma", sans-serif; font-size: 6px;
    line-height: 1.35; color: var(--brand-blue); text-align: center; }
  .back-brand .dot { display: block; width: 14px; height: 14px; border-radius: 50%; background: var(--brand-blue); margin: 0 auto 4px; }
  .stamp-box { position: absolute; left: 706px; top: 17px; width: 70px; height: 70px; border: 1.5px solid var(--ink); }
  .address-line { position: absolute; left: 576px; width: 200px; height: 1.5px; background: var(--ink); }
</style>
</head>
<body>

<section class="card card-front" aria-label="Postcard front">
  <div class="front-photo" role="img" aria-label="Photo of a stucco home entrance with an arched wooden double door with iron grilles, flanked by cypress trees, a paved walkway leading up"></div>
  <svg class="front-overlay" width="793" height="510" viewBox="0 0 793 510">
    <path d="M0 0 H793 V510 H0 Z M24 21 V230 C24 330 120 395 240 395 H770 V21 Z" fill="#eef2ec" fill-rule="evenodd" opacity="0.85"/>
    <path d="M46 36 H749 V380 H250 C140 380 46 320 46 230 Z" fill="none" stroke="#ffffff" stroke-width="2"/>
  </svg>
  <h1 class="tagline">Design the smile your home deserves</h1>
  <div class="front-brand"><span class="dot"></span>WROUGHT GATE STUDIO</div>
  <p class="slogan">Distinctive style</p>
  <p class="front-phone">
    <svg width="22" height="22" viewBox="0 0 24 24" aria-hidden="true"><path fill="#1a5a93" d="M6.6 10.8a15.1 15.1 0 0 0 6.6 6.6l2.2-2.2c.3-.3.7-.4 1-.2 1.1.4 2.3.6 3.6.6.6 0 1 .4 1 1V20c0 .6-.4 1-1 1A17 17 0 0 1 3 4c0-.6.4-1 1-1h3.5c.6 0 1 .4 1 1 0 1.3.2 2.5.6 3.6.1.3 0 .7-.2 1z"/></svg>
    (555)-318-2764
  </p>
  <p class="front-email">Dean@wroughtgatestudio.example</p>
</section>

<section class="card card-back" aria-label="Postcard back">
  <div class="message-side">
    <h2 class="headline">Lorem ipsum dolor sit amet, consectetuer adipiscing elit.</h2>
    <p class="body-copy">Lorem ipsum dolor sit amet, consectetuer adipiscing elit. Aenean commodo ligula eget dolor. Aenean massa. Cum sociis natoque penatibus et magnis dis parturient montes, nascetur ridiculus mus. Donec quam felis, ultricies nec, pellentesque eu, pretium quis, sem. Nulla consequat massa quis enim.</p>
    <div class="house-photo" role="img" aria-label="Photo of a single-storey home with a red tile roof, palm trees and a driveway"></div>

    <div class="info-band">
      <p class="col-left">Lorem ipsum dolor sit amet, consectetuer adipiscing elit. Aenean commodo ligula eget dolor. Aenean massa. Cum sociis natoque penatibus et magnis dis parturient montes, nascetur ridiculus mus. Donec quam felis, ultricies nec, pellentesque eu, pretium quis, sem. Nulla consequat massa quis enim.</p>
      <span class="divider"></span>
      <p class="col-right">Donec pede justo, fringilla vel, aliquet nec, vulputate eget, arcu. In enim justo, rhoncus ut, imperdiet a, venenatis vitae, justo.</p>
    </div>

    <p class="lower-copy">Lorem ipsum dolor sit amet, consectetuer adipiscing elit. Aenean commodo ligula eget dolor. Aenean massa. Cum sociis natoque penatibus et magnis dis parturient montes, nascetur ridicu</p>

    <div class="portrait" role="img" aria-label="Portrait photo of Dean Harlowe in a suit"></div>
    <p class="contact-name">Dean Harlowe</p>
    <p class="contact-phone">
      <svg width="13" height="13" viewBox="0 0 24 24" aria-hidden="true"><path fill="#1a5a93" d="M6.6 10.8a15.1 15.1 0 0 0 6.6 6.6l2.2-2.2c.3-.3.7-.4 1-.2 1.1.4 2.3.6 3.6.6.6 0 1 .4 1 1V20c0 .6-.4 1-1 1A17 17 0 0 1 3 4c0-.6.4-1 1-1h3.5c.6 0 1 .4 1 1 0 1.3.2 2.5.6 3.6.1.3 0 .7-.2 1z"/></svg>
      (555)-318-2764
    </p>
    <p class="contact-email">Dean@wroughtgatestudio.example</p>

    <div class="door-tile before" role="img" aria-label="Before photo: plain white paneled double door">
      <span class="label">BEFORE</span>
    </div>
    <div class="door-tile after" role="img" aria-label="After photo: ornate arched iron double door with holiday wreaths">
      <span class="label">AFTER</span>
    </div>
  </div>

  <div class="back-brand"><span class="dot"></span>WROUGHT GATE STUDIO</div>
  <div class="stamp-box"></div>
  <span class="address-line" style="top:248px"></span>
  <span class="address-line" style="top:278px"></span>
  <span class="address-line" style="top:309px"></span>
  <span class="address-line" style="top:338px"></span>
</section>

</body>
</html>
```